Photoshop Templates for Instagram, x 2

A Square template to reuse that is on brand.

It will involve an image and text of between 3 and 10 words.
I would like 2 separate contrasting images to use interchangeably

In the files I have added some of the images that I have been using, as well as the home page of my website that is currently being developed.

The on brand would be very recognisable with the website.

Requirements
Must have
• Must be similar in feel to the home page.

Must be simple to to change image and and text in the template

I would like 2 designs. Both similar, but contrasting

The square images show the look that I have been using (created by myself, so I'm sure these can be massively improved upon)

```html
<!DOCTYPE html>
<html lang="en">
<head>
<meta charset="utf-8">
<title>Quote Templates – Square Pair</title>
<link href="https://fonts.googleapis.com/css2?family=Mulish:wght@400;700;800&display=swap" rel="stylesheet">
<style>
  :root {
    --ink: #000000;
    --paper: #ffffff;
    --accent: #12a6e8;
    --photo-a: #2a3f8f;
    --photo-b: #a3213a;
    --photo-c: #1b2a55;
  }
  * { margin: 0; padding: 0; box-sizing: border-box; }
  html, body {
    width: 1200px; height: 587px; overflow: hidden;
    background: var(--paper);
    font-family: "Mulish", Arial, sans-serif;
  }
  .canvas { position: relative; width: 1200px; height: 587px; }
  .template {
    position: absolute; top: 0; width: 587px; height: 587px;
    background: var(--ink); overflow: hidden;
  }
  .template--chevron { left: 0; }
  .template--bracket { left: 614px; width: 586px; }
  .template svg.shapes { position: absolute; inset: 0; width: 100%; height: 100%; }
  .text-white { color: var(--paper); }
  .text-accent { color: var(--accent); }

  /* Chevron template */
  .chevron-quote {
    position: absolute; left: 0; width: 587px; text-align: center;
    font-weight: 700; font-size: 33px; line-height: 1; color: var(--paper);
    letter-spacing: -0.2px;
  }
  .chevron-quote.line-1 { top: 362px; }
  .chevron-quote.line-2 { top: 407px; }
  .chevron-quote.line-3 { top: 454px; }
  .author {
    font-weight: 400; font-size: 21px; line-height: 1; color: var(--paper);
    text-align: center; position: absolute;
  }
  .template--chevron .author { left: 0; width: 587px; top: 513px; }

  /* Bracket template */
  .photo-panel {
    position: absolute; left: 0; top: 0; width: 282px; height: 541px;
    background: linear-gradient(160deg, var(--photo-c) 0%, var(--photo-a) 35%, var(--photo-b) 60%, var(--photo-a) 85%, var(--photo-c) 100%);
  }
  .bracket-line {
    position: absolute; left: 300px; width: 300px; text-align: center;
    transform: translateY(-50%); line-height: 1; font-weight: 700;
    white-space: nowrap;
  }
  .bracket-line.size-m { font-size: 37px; }
  .bracket-line.size-s { font-size: 22px; }
  .bracket-line.size-l { font-size: 58px; font-weight: 800; }
  .bracket-line.size-xl { font-size: 48px; font-weight: 800; }
  .template--bracket .author { left: 300px; width: 300px; top: 441px; transform: translateY(-50%); }
</style>
</head>
<body>
<div class="canvas">

  <!-- Template 1: chevron -->
  <section class="template template--chevron">
    <svg class="shapes" viewBox="0 0 987 987" preserveAspectRatio="none">
      <polygon role="img" aria-label="Photo of a footballer celebrating, pointing forward"
        points="0,0 987,0 987,22 490,520 0,30" fill="url(#chevronPhoto)"/>
      <defs>
        <linearGradient id="chevronPhoto" x1="0" y1="0" x2="0.4" y2="1">
          <stop offset="0" stop-color="#1b2a55"/>
          <stop offset="0.45" stop-color="#2a3f8f"/>
          <stop offset="0.7" stop-color="#a3213a"/>
          <stop offset="1" stop-color="#2a3f8f"/>
        </linearGradient>
      </defs>
      <polygon class="chevron-band" points="190,258 232,258 490,516 752,258 795,258 490,558" fill="#12a6e8"/>
      <line x1="0" y1="770" x2="215" y2="990" stroke="#12a6e8" stroke-width="6"/>
      <line x1="987" y1="762" x2="765" y2="990" stroke="#12a6e8" stroke-width="6"/>
    </svg>
    <p class="chevron-quote line-1">YOU CAN <span class="text-accent">OVERCOME ANYTHING,</span></p>
    <p class="chevron-quote line-2">IF AND ONLY IF YOU</p>
    <p class="chevron-quote line-3"><span class="text-accent">LOVE</span> SOMETHING <span class="text-accent">ENOUGH</span></p>
    <p class="author">-DARIO VELCORTE</p>
  </section>

  <!-- Template 2: bracket -->
  <section class="template template--bracket">
    <div class="photo-panel" role="img" aria-label="Photo of a footballer celebrating, pointing forward"></div>
    <svg class="shapes" viewBox="0 0 586 587">
      <rect x="282" y="257" width="17" height="299" fill="#12a6e8"/>
      <rect x="200" y="540" width="99" height="16" fill="#12a6e8"/>
    </svg>
    <p class="bracket-line size-m text-white" style="top:122px">YOU CAN</p>
    <p class="bracket-line size-m text-accent" style="top:161px">OVERCOME</p>
    <p class="bracket-line size-m text-accent" style="top:201px">ANYTHING,</p>
    <p class="bracket-line size-s text-white" style="top:237px">IF AND ONLY IF YOU</p>
    <p class="bracket-line size-l text-accent" style="top:283px">LOVE</p>
    <p class="bracket-line size-m text-white" style="top:337px">SOMETHING</p>
    <p class="bracket-line size-xl text-accent" style="top:387px">ENOUGH</p>
    <p class="author">-DARIO VELCORTE</p>
  </section>

</div>
</body>
</html>
```